Rehab/fitness Business card design

I need a design that promotes "A ready made base for runners". services include assessment, massage, physiotherapy, pilates, suspension training, kinesiotaping in any combination.
I would like to bring the design into my website, flyers etc

Target Market(s)

athletes from beginner to elite - any age, male and female

Industry/Entity Type

Shop

Contact Information for Business Card

Ready-Made-Base for Runners
17 Parvel Crescent, Hollowmere, Tauranga
021 847 3610
gwen.farrowby@quillmail.test

Logo Text

Requirements
Nice to have
• Blue colour theme

```html
<!DOCTYPE html>
<html lang="en">
<head>
<meta charset="utf-8">
<title>Ready-Made-Base for Runners – Business Card</title>
<link rel="stylesheet" href="https://fonts.googleapis.com/css2?family=Lato:wght@300;400;700&display=swap">
<style>
  :root {
    --navy: #0b3a6a;
    --mid-blue: #0f5a9c;
    --light-blue: #4a8fd0;
    --white: #ffffff;
    --backdrop: #e9edf1;
    --ink: #0d3a6a;
  }
  * { margin: 0; padding: 0; box-sizing: border-box; }
  html, body { width: 1200px; height: 1000px; overflow: hidden; }
  body {
    background: var(--backdrop);
    font-family: "Lato", Arial, sans-serif;
    position: relative;
  }
  .card {
    position: absolute;
    top: 350px;
    width: 536px;
    height: 300px;
    background: var(--white);
    border-radius: 9px;
    overflow: hidden;
    box-shadow: 3px 4px 10px rgba(0,0,0,0.28);
  }
  .card--front { left: 46px; }
  .card--back { left: 617px; }
  .card__waves { position: absolute; inset: 0; width: 536px; height: 300px; }
  .brand {
    position: absolute;
    left: 35px;
    top: 44px;
    color: var(--ink);
    font-weight: 700;
    font-size: 23px;
    letter-spacing: -0.2px;
    white-space: nowrap;
  }
  .brand__tagline { font-weight: 300; font-size: 15px; letter-spacing: 0; }
  .contact {
    position: absolute;
    right: 30px;
    top: 190px;
    list-style: none;
    color: var(--white);
    font-size: 14px;
    font-weight: 400;
  }
  .contact__item {
    display: flex;
    justify-content: flex-end;
    align-items: center;
    gap: 8px;
    height: 28px;
  }
  .contact__icon { width: 18px; height: 18px; }
  .services {
    position: absolute;
    left: 34px;
    top: 31px;
    list-style: none;
    color: var(--ink);
    font-size: 19.5px;
    line-height: 26px;
  }
  .services li::before { content: "•"; margin-right: 6px; }
  .combination {
    position: absolute;
    right: 33px;
    top: 242px;
    color: var(--white);
    font-size: 23px;
    font-weight: 400;
  }
</style>
</head>
<body>

<section class="card card--front" aria-label="Business card front">
  <svg class="card__waves" viewBox="0 0 536 300" aria-hidden="true">
    <path fill="var(--light-blue)" d="M0,168 C60,182 100,185 140,184 C280,178 420,96 536,96 V300 H0 Z"/>
    <path fill="var(--white)" d="M0,168 C60,182 100,185 140,184 C285,178 425,112 536,113 V300 H0 Z"/>
    <path fill="var(--mid-blue)" d="M0,168 C60,182 100,185 140,184 C290,178 430,116 536,117 V300 H0 Z"/>
    <path fill="var(--white)" d="M0,168 C60,182 100,185 140,184 C300,180 440,132 536,134 V300 H0 Z"/>
    <path fill="var(--navy)" d="M0,168 C60,182 100,185 140,184 C310,182 450,144 536,150 V300 H0 Z"/>
  </svg>
  <h1 class="brand">Ready-Made-Base <span class="brand__tagline">for Runners</span></h1>
  <ul class="contact">
    <li class="contact__item">021 847 3610
      <svg class="contact__icon" viewBox="0 0 18 18" aria-hidden="true"><circle cx="9" cy="9" r="8" fill="none" stroke="#fff" stroke-width="1.3"/><path fill="#fff" d="M6 4.5 L7.6 6.6 L6.8 7.6 C7.5 9 8.7 10.3 10.2 11 L11.2 10.2 L13.3 11.8 L12.4 13.2 C9 13 5 9 4.8 5.5 Z"/></svg>
    </li>
    <li class="contact__item">gwen.farrowby@quillmail.test
      <svg class="contact__icon" viewBox="0 0 18 18" aria-hidden="true"><circle cx="9" cy="9" r="8" fill="none" stroke="#fff" stroke-width="1.3"/><text x="9" y="12.5" text-anchor="middle" fill="#fff" font-family="Lato, Arial, sans-serif" font-size="10" font-weight="700">@</text></svg>
    </li>
    <li class="contact__item">17 Parvel Crescent, Hollowmere
      <svg class="contact__icon" viewBox="0 0 18 18" aria-hidden="true"><circle cx="9" cy="9" r="8" fill="none" stroke="#fff" stroke-width="1.3"/><path fill="#fff" d="M9 3.8 C6.8 3.8 5.5 5.4 5.5 7.2 C5.5 9.6 9 14 9 14 C9 14 12.5 9.6 12.5 7.2 C12.5 5.4 11.2 3.8 9 3.8 Z M9 5.8 A1.4 1.4 0 1 1 9 8.6 A1.4 1.4 0 1 1 9 5.8 Z"/></svg>
    </li>
  </ul>
</section>

<section class="card card--back" aria-label="Business card back">
  <svg class="card__waves" viewBox="0 0 536 300" aria-hidden="true">
    <path fill="var(--light-blue)" d="M0,205 C40,215 80,220 100,220 C250,218 420,133 536,133 V300 H0 Z"/>
    <path fill="var(--white)" d="M0,205 C40,215 80,220 100,220 C255,218 425,147 536,147 V300 H0 Z"/>
    <path fill="var(--mid-blue)" d="M0,205 C40,215 80,220 100,220 C260,218 428,150 536,150 V300 H0 Z"/>
    <path fill="var(--white)" d="M0,205 C40,215 80,220 100,220 C270,219 435,163 536,165 V300 H0 Z"/>
    <path fill="var(--navy)" d="M0,205 C40,215 80,220 100,220 C280,220 445,174 536,178 V300 H0 Z"/>
  </svg>
  <ul class="services">
    <li>assessment</li>
    <li>massage</li>
    <li>physiotherapy</li>
    <li>pilates</li>
    <li>suspension training</li>
    <li>kinesiotaping</li>
  </ul>
  <p class="combination">in any combination</p>
</section>

</body>
</html>
```